Real Estate Team Business Card

We need a business card designed for our real estate team called "Larkspur Realty Group". We would like to receive a final format that would allow us to edit the contact information for new employees as they are added to our team. The difficult part of the design is that we will need to have two logos on the card - both our team name logo for "Larkspur Realty Group" and our company logo for "Corvane Real Estate". Most emphasis should be given to the team logo - maybe double the size of our company logo. (we just have to have the company logo somewhere on the card for legal purposes) The design should somehow illustrate we work in real estate, but still use the beehive/bee concept as a lot of our marketing will involve "bee" sayings. We would also like to use the tagline: "find out what all the buzz is about". We also need to use the "fair housing" logo and "realtor" logos. These can both be small like the company logo.
Target Market(s)
Real Estate
Industry/Entity Type
Real Estate Agent
Contact Information for Business Card
Name: Dylan Marsh Title: Realtor Phone: 801-555-0172 Email: dylan@larkspurrealtrygroup.com Website: www.larkspurrealtygroup.com Facebook: fb/me/larkspurrealtygroup Twitter: @LarkspurRltyGrp
Colors
Designer to choose colors to be used in the design.
Requirements
Must have
- Contact information. Larkspur Realty Group Logo. Corvane Real Estate Logo. Realtor logo. Fair Housing Logo. Tagline: "find out what all the buzz is about".
Nice to have
- It would be nice to illustrate that we work in real estate. It would also be nice to somehow incorporate bees or play off of our beehive logo. We will do a lot of marking using sayings like "let us bee the solution" or "real estate meant to bee" etc.

```html
<!DOCTYPE html>
<html lang="en">
<head>
<meta charset="utf-8">
<title>Larkspur Realty Group – Business Card</title>
<link rel="stylesheet" href="https://fonts.googleapis.com/css2?family=Montserrat:wght@500;600;700&family=Source+Sans+3:wght@400;600;700&display=swap">
<style>
  :root {
    --page-bg: #e4e4e2;
    --honey: #f7c600;
    --honey-light: #fcd21a;
    --ink: #111111;
    --paper: #f2f2f2;
    --paper-edge: #e6e6e6;
    --muted: #8a8a8a;
    --back-black: #050505;
    --white: #ffffff;
  }
  * { margin: 0; padding: 0; box-sizing: border-box; }
  html, body { width: 1200px; height: 1176px; overflow: hidden; }
  body {
    background: var(--page-bg);
    font-family: "Source Sans 3", "Helvetica Neue", Arial, sans-serif;
    color: var(--ink);
    position: relative;
  }
  .card {
    position: absolute;
    left: 199px;
    width: 786px;
    height: 448px;
    border-radius: 22px;
    overflow: hidden;
  }
  .card-front { top: 84px; background: linear-gradient(180deg, var(--honey-light), var(--honey)); }
  .card-back { top: 592px; background: var(--back-black); }

  /* front: white contact panel with notched edge */
  .contact-panel {
    position: absolute;
    inset: 0 0 0 376px;
    background: linear-gradient(180deg, #fafafa, var(--paper) 60%, var(--paper-edge));
    clip-path: polygon(18px 0, 100% 0, 100% 100%, 18px 100%, 18px 326px, 0 306px, 0 136px, 18px 116px);
  }
  .agent-name {
    position: absolute; left: 432px; top: 64px;
    font-family: "Montserrat", Arial, sans-serif;
    font-weight: 700; font-size: 23px; letter-spacing: 0.3px;
  }
  .agent-title {
    position: absolute; left: 432px; top: 91px;
    font-size: 18px; color: var(--honey); letter-spacing: 0.3px;
  }
  .title-rule {
    position: absolute; left: 432px; right: 0; top: 124px;
    height: 3px; background: var(--honey);
  }
  .contact-list { position: absolute; left: 382px; top: 142px; list-style: none; }
  .contact-list li {
    display: flex; align-items: center;
    height: 35.5px; font-size: 18px;
  }
  .contact-icon { width: 16px; height: 16px; margin-right: 34px; flex: none; }
  .contact-icon svg { display: block; width: 16px; height: 16px; }
  .company-name {
    position: absolute; right: 48px; top: 352px;
    font-family: "Montserrat", Arial, sans-serif;
    font-weight: 600; font-size: 20px; color: var(--ink);
  }

  /* front: team identity on yellow */
  .team-identity {
    position: absolute; left: 0; width: 392px; top: 118px;
    display: flex; flex-direction: column; align-items: center;
  }
  .identity-mark { width: 74px; height: 74px; border-radius: 50%; background: var(--ink); }
  .team-name {
    margin-top: 18px; text-align: center;
    font-family: "Montserrat", Arial, sans-serif;
    font-weight: 600; font-size: 30px; line-height: 1.15;
    letter-spacing: 2px; text-transform: uppercase;
    color: var(--ink);
  }
  .badges {
    position: absolute; top: 352px; left: 148px;
    display: flex; gap: 22px;
  }
  .badge { width: 38px; height: 40px; background: var(--ink); }

  /* back */
  .back-identity {
    position: absolute; inset: 0;
    display: flex; flex-direction: column; align-items: center; justify-content: center;
  }
  .back-mark { width: 104px; height: 104px; border-radius: 50%; background: var(--honey); }
  .back-name {
    margin-top: 30px; text-align: center;
    font-family: "Montserrat", Arial, sans-serif;
    font-weight: 600; font-size: 40px; line-height: 1.15;
    letter-spacing: 3px; text-transform: uppercase;
    color: var(--white);
  }
</style>
</head>
<body>

<section class="card card-front">
  <div class="team-identity">
    <div class="identity-mark"></div>
    <p class="team-name">Larkspur<br>Realty Group</p>
  </div>
  <div class="badges">
    <div class="badge"></div>
    <div class="badge"></div>
  </div>

  <div class="contact-panel"></div>
  <h1 class="agent-name">DYLAN MARSH</h1>
  <p class="agent-title">REALOR</p>
  <div class="title-rule"></div>

  <ul class="contact-list">
    <li><span class="contact-icon"><svg viewBox="0 0 16 16"><path fill="#f7c600" d="M1 6c0-2 3-3 7-3s7 1 7 3v1h-4V5.5H5V7H1zM3 8h10l1 5H2z"/><circle cx="8" cy="10.5" r="1.6" fill="#f2f2f2"/></svg></span>801-555-0172</li>
    <li><span class="contact-icon"><svg viewBox="0 0 16 16"><rect x="1" y="3" width="14" height="10" fill="#f7c600"/><path d="M1 3l7 6 7-6" fill="none" stroke="#f2f2f2" stroke-width="1.3"/></svg></span>dylan@larkspurrealtrygroup.com</li>
    <li><span class="contact-icon"><svg viewBox="0 0 16 16" fill="none" stroke="#f7c600" stroke-width="1.2"><circle cx="8" cy="8" r="6.5"/><ellipse cx="8" cy="8" rx="3" ry="6.5"/><path d="M1.5 8h13M2.5 4.5h11M2.5 11.5h11"/></svg></span>www.larkspurrealtygroup.com</li>
    <li><span class="contact-icon"><svg viewBox="0 0 16 16"><rect x="1" y="1" width="14" height="14" rx="2" fill="#f7c600"/></svg></span>fb/me/larkspurrealtygroup</li>
    <li><span class="contact-icon"><svg viewBox="0 0 16 16"><rect x="1" y="1" width="14" height="14" rx="2" fill="#f7c600"/></svg></span>@LarkspurRltyGrp</li>
  </ul>

  <p class="company-name">Corvane Real Estate</p>
</section>

<section class="card card-back">
  <div class="back-identity">
    <div class="back-mark"></div>
    <p class="back-name">Larkspur<br>Realty Group</p>
  </div>
</section>

</body>
</html>
```